Pinecrest Premier Motors *

Professional business cards for our auto wholesale dealership.

Target Market(s)

New and used cars sales managers and middle class to higher end private party buyers.

Industry/Entity Type

Automotive

Contact Information for Business Card

Pinecrest Premier Motors
Marcus T Holloran
Owner
(555) 014-3862
pineprem@mailvista.example
Dealer Lic # 48265

Logo Text

Pinecrest Premier Motors, Pine Prem Motors, PPM, etc

Font styles to use
Serif
Sans Serif

Colors

Designer to choose colors to be used in the design.

Requirements
Must have
• A professional, but not pretentious, look
Nice to have
• It might be nice to see "PPM" in a shape form i.e. circle, triangle, etc in the corner or background somehwere
Should not have
• bright "girly" colors

```html
<!DOCTYPE html>
<html lang="en">
<head>
<meta charset="utf-8">
<title>Pinecrest Premier Motors — Business Card</title>
<link rel="stylesheet" href="https://fonts.googleapis.com/css2?family=Open+Sans:wght@800&family=Ubuntu:wght@400;500&display=swap">
<style>
  :root {
    --bg: #2c2d30;
    --card-dark: #262b34;
    --card-dark-edge: #1d2128;
    --card-light: #f4f4f4;
    --card-light-edge: #d9d9d9;
    --lime: #a9d20f;
    --lime-deep: #8db50a;
    --ink: #2b2f36;
    --ink-soft: #1c2027;
    --paper-text: #f2f3f5;
  }
  * { box-sizing: border-box; margin: 0; padding: 0; }
  html, body { width: 1200px; height: 1200px; overflow: hidden; }
  body {
    background: var(--bg);
    position: relative;
    font-family: "Ubuntu", sans-serif;
  }
  .card {
    position: absolute;
    left: 250px;
    width: 700px;
    height: 400px;
    border-radius: 26px;
    overflow: hidden;
    box-shadow: 0 18px 40px rgba(0,0,0,.45);
  }

  /* Front */
  .card--front {
    top: 160px;
    background: linear-gradient(135deg, #ffffff 0%, var(--card-light) 55%, var(--card-light-edge) 100%);
  }
  .front-mark {
    position: absolute;
    left: 0; right: 0; top: 110px;
    display: flex;
    flex-direction: column;
    align-items: center;
    gap: 26px;
  }
  .front-mark__dot {
    width: 110px; height: 110px;
    border-radius: 50%;
    background: radial-gradient(circle at 35% 35%, var(--lime) 0%, var(--lime-deep) 100%);
  }
  .front-mark__name {
    font-family: "Open Sans", sans-serif;
    font-weight: 800;
    font-size: 42px;
    color: var(--ink);
    letter-spacing: .5px;
  }

  /* Back */
  .card--back {
    top: 640px;
    background: linear-gradient(160deg, #2f3541 0%, var(--card-dark) 50%, var(--card-dark-edge) 100%);
  }
  .back-mark {
    position: absolute;
    left: 60px; top: 50px;
    display: flex;
    align-items: center;
    gap: 22px;
  }
  .back-mark__dot {
    width: 150px; height: 150px;
    border-radius: 50%;
    background: radial-gradient(circle at 35% 35%, #b9dd16 0%, var(--lime-deep) 100%);
  }
  .back-mark__name {
    font-weight: 500;
    font-size: 34px;
    color: var(--paper-text);
    letter-spacing: 2px;
  }
  .name-tag {
    position: absolute;
    right: 0; top: 150px;
    width: 330px; height: 78px;
    border-radius: 22px 0 0 22px;
    background: linear-gradient(90deg, #c8e210 0%, var(--lime) 60%, var(--lime-deep) 100%);
    display: flex;
    flex-direction: column;
    justify-content: center;
    align-items: center;
    color: var(--ink-soft);
  }
  .name-tag__name { font-size: 29px; font-weight: 500; line-height: 1.1; }
  .name-tag__role { font-size: 19px; font-weight: 500; }
  .contact {
    position: absolute;
    right: 40px; top: 252px;
    list-style: none;
    display: flex;
    flex-direction: column;
    align-items: flex-end;
    gap: 12px;
    color: var(--paper-text);
    font-size: 21px;
  }
  .contact__item { display: flex; align-items: center; gap: 14px; height: 26px; }
  .contact__icon { width: 24px; height: 24px; flex: none; }
  .contact__spacer { width: 24px; flex: none; }
  .accent-band {
    position: absolute;
    left: 0; bottom: 0;
    width: 640px; height: 26px;
    border-radius: 0 14px 0 0;
    background: linear-gradient(90deg, var(--lime-deep) 0%, var(--lime) 100%);
  }
</style>
</head>
<body>
  <section class="card card--front" aria-label="Card front">
    <div class="front-mark">
      <div class="front-mark__dot"></div>
      <div class="front-mark__name">Pinecrest Premier Motors</div>
    </div>
  </section>

  <section class="card card--back" aria-label="Card back">
    <div class="back-mark">
      <div class="back-mark__dot"></div>
      <div class="back-mark__name">PPM</div>
    </div>

    <div class="name-tag">
      <span class="name-tag__name">Marcus T Holloran</span>
      <span class="name-tag__role">Owner</span>
    </div>

    <ul class="contact">
      <li class="contact__item">
        <span>(555) 014-3862</span>
        <svg class="contact__icon" viewBox="0 0 24 24" aria-hidden="true">
          <path fill="#a9d20f" d="M6.6 10.8a15.1 15.1 0 0 0 6.6 6.6l2.2-2.2c.3-.3.7-.4 1-.2 1.1.4 2.3.6 3.6.6.6 0 1 .4 1 1V20c0 .6-.4 1-1 1A17 17 0 0 1 3 4c0-.6.4-1 1-1h3.5c.6 0 1 .4 1 1 0 1.3.2 2.5.6 3.6.1.3 0 .7-.2 1z"/>
        </svg>
      </li>
      <li class="contact__item">
        <span>pineprem@mailvista.example</span>
        <svg class="contact__icon" viewBox="0 0 24 24" aria-hidden="true">
          <rect x="2" y="5" width="20" height="14" rx="1.5" fill="none" stroke="#a9d20f" stroke-width="2"/>
          <path d="M3 6l9 7 9-7" fill="none" stroke="#a9d20f" stroke-width="2"/>
        </svg>
      </li>
      <li class="contact__item">
        <span>Dealer Lic # 48265</span>
        <span class="contact__spacer"></span>
      </li>
    </ul>

    <div class="accent-band"></div>
  </section>
</body>
</html>
```